Quillmere business card

We're looking to "refresh" our original Quillmere logo design and also get a new business card design. We're a modern consulting and software business that's been around 4-years now. We work with large professional companies and therefore require a design that is simple and professional. We would like to retain the notch in the "A" and just the word "Quillmere" as the logo. We like greys, silvers, black, white...but happy to explore highlight color. We're looking for understated modern.

Industry/Entity Type

Software

```html
<!DOCTYPE html>
<html lang="en">
<head>
<meta charset="utf-8">
<title>Quillmere business card</title>
<link rel="stylesheet" href="https://fonts.googleapis.com/css2?family=Barlow:wght@400;700&display=swap">
<style>
  :root {
    --stage: #dfe1e3;
    --card-white: #f7f8f9;
    --card-blue: #1f6db3;
    --card-blue-deep: #185a97;
    --ink: #2f3133;
    --ink-soft: #4a4d50;
    --accent: #1f6db3;
    --on-blue: #ffffff;
  }
  * { box-sizing: border-box; margin: 0; padding: 0; }
  html, body { width: 1200px; height: 900px; overflow: hidden; }
  body {
    background: var(--stage);
    font-family: "Barlow", "Helvetica Neue", Arial, sans-serif;
    display: flex;
    flex-direction: column;
    align-items: center;
    justify-content: center;
    gap: 48px;
  }
  .card {
    width: 580px;
    height: 354px;
    position: relative;
    border-radius: 4px;
    overflow: hidden;
    box-shadow: 0 6px 18px rgba(0,0,0,0.12);
  }
  /* Front */
  .card--front {
    background: linear-gradient(120deg, var(--card-white) 60%, #e9ecef 100%);
    color: var(--ink);
    padding: 58px 56px;
  }
  .wordmark {
    font-weight: 700;
    letter-spacing: -0.5px;
    line-height: 1;
  }
  .card--front .wordmark { font-size: 64px; color: var(--ink); }
  .contact-name {
    margin-top: 52px;
    font-size: 21px;
    color: var(--ink);
    display: flex;
    align-items: center;
    gap: 16px;
  }
  .contact-name .dot {
    width: 8px; height: 8px; border-radius: 50%;
    background: var(--accent);
  }
  .contact-list {
    list-style: none;
    margin-top: 22px;
    font-size: 17px;
    color: var(--ink-soft);
  }
  .contact-list li {
    display: flex;
    align-items: center;
    gap: 14px;
    height: 26px;
  }
  .contact-list svg { width: 14px; height: 14px; flex: none; fill: var(--accent); }
  /* Back */
  .card--back {
    background: linear-gradient(135deg, var(--card-blue-deep) 0%, var(--card-blue) 55%, #2478c2 100%);
    color: var(--on-blue);
    display: flex;
    flex-direction: column;
    align-items: flex-end;
    justify-content: flex-end;
    padding: 0 44px 58px;
  }
  .card--back .wordmark { font-size: 68px; color: var(--on-blue); }
  .web-address {
    margin-top: 10px;
    font-size: 17px;
    letter-spacing: 0.5px;
  }
</style>
</head>
<body>
  <section class="card card--front" aria-label="Business card front">
    <div class="wordmark">Quillmere</div>
    <p class="contact-name"><span class="dot"></span>Daniel Hartley, director</p>
    <ul class="contact-list">
      <li>
        <svg viewBox="0 0 14 14" aria-hidden="true"><path d="M4 0h6a1.5 1.5 0 0 1 1.5 1.5v11A1.5 1.5 0 0 1 10 14H4a1.5 1.5 0 0 1-1.5-1.5v-11A1.5 1.5 0 0 1 4 0zm0 1.6v9.4h6V1.6zM7 11.6a.8.8 0 1 0 0 1.6.8.8 0 0 0 0-1.6z"/></svg>
        0400 555 019
      </li>
      <li>
        <svg viewBox="0 0 14 14" aria-hidden="true"><path d="M0 3h14v9H0zm1.4 1.3v.3L7 8.2l5.6-3.6v-.3zm0 1.9v4.5h11.2V6.2L7 9.8z"/></svg>
        dhartley@quillmere.com.au
      </li>
      <li>
        <svg viewBox="0 0 14 14" aria-hidden="true"><path d="M7 0a5 5 0 0 1 5 5c0 3.5-5 9-5 9S2 8.5 2 5a5 5 0 0 1 5-5zm0 3a2 2 0 1 0 0 4 2 2 0 0 0 0-4z"/></svg>
        PO Box 456, Harbour NSW 1240
      </li>
    </ul>
  </section>

  <section class="card card--back" aria-label="Business card back">
    <div class="wordmark">Quillmere</div>
    <p class="web-address">www.quillmere.com.au</p>
  </section>
</body>
</html>
```